Full service residential and commercial painting
Finest quality attention to detail
All workmanship guaranteed
Email :norabvantreel@mailbox-example.fr
Mobile: 0417382650
Industry/Entity Type
Residential
Contact Information for Business Card
Henri marsot painting & decorating
Requirements
Nice to have
- Am thinking about someone can be painting my name on the card with HM painting with the logos of brush,pot tray and roller sleeves

```html
<!DOCTYPE html>
<html lang="en">
<head>
<meta charset="utf-8">
<title>HM painting – business card</title>
<link rel="stylesheet" href="https://fonts.googleapis.com/css2?family=Open+Sans:wght@400;600&display=swap">
<style>
  :root {
    --backdrop: #e4e4e4;
    --card-white: #ffffff;
    --umber: #5e574b;
    --tan: #c2a56f;
    --ink: #4a463f;
    --contact-text: #f2efe9;
  }
  * { margin: 0; padding: 0; box-sizing: border-box; }
  html, body {
    width: 1200px; height: 985px; overflow: hidden;
    background: var(--backdrop);
    font-family: "Open Sans", sans-serif;
  }
  .card {
    position: absolute; left: 100px; top: 206px;
    width: 1000px; height: 572px;
    border-radius: 28px; overflow: hidden;
    background: var(--card-white);
    box-shadow: 0 10px 30px rgba(0,0,0,.18);
  }
  .card-shapes { position: absolute; inset: 0; }
  .brand {
    position: absolute; left: 150px; top: 112px;
    display: flex; align-items: center; gap: 22px;
  }
  .brand-mark { width: 58px; height: 58px; background: var(--tan); }
  .brand-name {
    font-size: 74px; font-weight: 400; color: var(--umber);
    letter-spacing: 1px; line-height: 1;
  }
  .services {
    position: absolute; left: 400px; top: 232px;
    list-style: none; color: var(--ink);
    font-size: 21px; line-height: 32px; white-space: nowrap;
  }
  .services li { display: flex; align-items: center; gap: 12px; }
  .services svg { width: 20px; height: 20px; flex: none; }
  .contact {
    position: absolute; left: 90px; top: 372px;
    color: var(--contact-text); font-size: 25px; line-height: 34px;
  }
  .contact-line { display: flex; align-items: center; gap: 14px; }
  .contact-line svg { width: 20px; height: 20px; flex: none; }
  .contact-line .spacer { width: 20px; }
</style>
</head>
<body>
  <article class="card">
    <svg class="card-shapes" viewBox="0 0 1000 572" preserveAspectRatio="none" aria-hidden="true">
      <rect x="0" y="350" width="1000" height="222" fill="var(--umber)"/>
      <polygon points="0,0 90,0 90,150 60,190 60,350 0,350" fill="var(--umber)"/>
      <polygon points="0,350 60,350 60,450 0,480" fill="var(--tan)"/>
      <line x1="60" y1="190" x2="90" y2="150" stroke="#fff" stroke-width="4"/>
    </svg>

    <div class="brand">
      <span class="brand-mark"></span>
      <span class="brand-name">HM painting</span>
    </div>

    <ul class="services">
      <li><svg viewBox="0 0 22 22"><rect x="1" y="3" width="18" height="18" fill="none" stroke="var(--tan)" stroke-width="2"/><path d="M5 11l5 5 10-13" fill="none" stroke="var(--umber)" stroke-width="3"/></svg>Full service residential and commercial painting</li>
      <li><svg viewBox="0 0 22 22"><rect x="1" y="3" width="18" height="18" fill="none" stroke="var(--tan)" stroke-width="2"/><path d="M5 11l5 5 10-13" fill="none" stroke="var(--umber)" stroke-width="3"/></svg>Finest quality attention to detail</li>
      <li><svg viewBox="0 0 22 22"><rect x="1" y="3" width="18" height="18" fill="none" stroke="var(--tan)" stroke-width="2"/><path d="M5 11l5 5 10-13" fill="none" stroke="var(--umber)" stroke-width="3"/></svg>All workmanship guaranteed</li>
    </ul>

    <div class="contact">
      <p class="contact-line"><span class="spacer"></span>Henri marsot painting &amp; decorating</p>
      <p class="contact-line"><svg viewBox="0 0 20 20" aria-label="Phone"><rect width="20" height="20" fill="var(--umber)" stroke="#fff" stroke-width="1.5"/><path d="M6 4c-2 2 0 7 4 10 2 2 4 2 5 1l-2-3-2 1c-1-1-3-3-3-4l1-2z" fill="#fff"/></svg>0417382650</p>
      <p class="contact-line"><svg viewBox="0 0 20 20" aria-label="Email"><rect x="1" y="4" width="18" height="12" fill="none" stroke="#fff" stroke-width="1.5"/><path d="M1 4l9 7 9-7" fill="none" stroke="#fff" stroke-width="1.5"/></svg>norabvantreel@mailbox-example.fr</p>
    </div>
  </article>
</body>
</html>
```